Full service meeting planning company needs new business cards

Bright Harbor is a full service meeting planning company that specializes in on-line conference registration web development and event communications. We combine citywide hotel management, mobile applications, eblast reminders, confirmation letters, and customized reporting to create a seamless registration process. We also manage group motor coach transportation, food and beverages, entertainment, stage and lighting for group of 10 to 4000.

Target Market(s)

Corporations and associations

Industry/Entity Type

Event Planning

Contact Information for Business Card

standard size 3.5" wide and 2" tall

Font styles to use
Serif
Sans Serif

Colors
f37122
f78f20
333333
5c5c5c
9d9d9d
f68d4d

Requirements
Must have
• {name}
• Bright Harbor
• P.O. Box 7384, Grand Rapids, M I 49577
• www.brightharborplan.com
• {email}
• {phone}
• {mobile phone}
Nice to have
• Our colors are black, grey and orange as an accent color
Should not have
• I am not happy with our website layout anymore either. It feels dark and old but it does explain who we are pretty well if you'd like to review; www.brightharborplan.com

```html
<!DOCTYPE html>
<html lang="en">
<head>
<meta charset="utf-8">
<title>Bright Harbor – Business Cards</title>
<link href="https://fonts.googleapis.com/css2?family=Montserrat:wght@400;500;700&display=swap" rel="stylesheet">
<style>
  :root {
    --backdrop: #2b2b2b;
    --card-black: #000000;
    --band-grey: #5c5c5c;
    --accent-orange: #f37122;
    --accent-orange-light: #f78f20;
    --text-white: #ffffff;
    --text-soft: #e6e6e6;
  }
  * { margin: 0; padding: 0; box-sizing: border-box; }
  html, body {
    width: 1200px; height: 900px; overflow: hidden;
    background: var(--backdrop);
    font-family: "Montserrat", sans-serif;
  }
  .canvas {
    position: relative; width: 1200px; height: 900px;
  }
  .card {
    position: absolute; left: 337px;
    width: 525px; height: 300px;
    border-radius: 22px;
    background: var(--card-black);
    overflow: hidden;
    box-shadow: 0 14px 30px rgba(0,0,0,0.45);
  }
  .card-front { top: 110px; }
  .card-back { top: 490px; }

  /* Front */
  .front-wordmark {
    position: absolute; left: 60px; top: 120px;
    font-weight: 700; font-size: 42px; letter-spacing: 1px;
    color: var(--accent-orange-light);
  }
  .front-web {
    position: absolute; right: 40px; bottom: 34px;
    font-size: 15px; color: var(--text-white); font-weight: 400;
  }
  .front-web b { font-weight: 700; }

  /* Back */
  .band-left {
    position: absolute; left: 0; top: 0; bottom: 0; width: 118px;
    background: var(--band-grey);
  }
  .band-right {
    position: absolute; right: 0; top: 74px; bottom: 0; width: 22px;
    background: var(--band-grey);
  }
  .mark {
    position: absolute; left: 74px; top: 150px;
    width: 88px; height: 88px; border-radius: 50%;
    background: var(--accent-orange-light);
  }
  .mark-name {
    position: absolute; left: 172px; top: 184px;
    font-size: 13px; font-weight: 700; letter-spacing: 1px;
    color: var(--accent-orange-light);
  }
  .back-wordmark {
    position: absolute; right: 34px; top: 26px;
    font-weight: 700; font-size: 38px; letter-spacing: 0.5px;
    color: var(--text-white);
  }
  .contact {
    position: absolute; right: 46px; top: 92px;
    text-align: right; color: var(--text-soft);
    font-size: 12.5px; line-height: 1.38;
  }
  .contact .person {
    font-size: 21px; font-weight: 700; color: var(--accent-orange-light);
    line-height: 1.1;
  }
  .contact .role { margin-bottom: 10px; }
  .contact .gap { margin-top: 8px; }
  .contact .domain { color: var(--accent-orange-light); font-weight: 500; }
  .icons {
    position: absolute; right: 26px; top: 198px;
    display: flex; flex-direction: column; gap: 5px;
  }
  .icons svg { width: 12px; height: 12px; display: block; }
</style>
</head>
<body>
<main class="canvas">
  <section class="card card-front" aria-label="Card front">
    <div class="front-wordmark">BRIGHT HARBOR</div>
    <div class="front-web">www.<b>brightharborplan</b>.com</div>
  </section>

  <section class="card card-back" aria-label="Card back">
    <div class="band-left"></div>
    <div class="band-right"></div>
    <div class="mark"></div>
    <div class="mark-name">BRIGHT HARBOR</div>
    <div class="back-wordmark">BRIGHT HARBOR</div>
    <div class="contact">
      <div class="person">Marla Tennant</div>
      <div class="role">Director</div>
      <div>P.O. Box 7384</div>
      <div>Grand Rapids, M I 49577</div>
      <div class="gap">(616) 555-0142</div>
      <div>(616) 555-0178</div>
      <div>info@brightharborplan.com</div>
      <div>www.<span class="domain">brightharborplan</span>.com</div>
    </div>
    <div class="icons">
      <svg viewBox="0 0 12 12" aria-label="Phone"><path d="M2 1h2.5l1 3-1.5 1a6 6 0 0 0 3 3l1-1.5 3 1V10a1 1 0 0 1-1 1A9 9 0 0 1 1 2a1 1 0 0 1 1-1z" fill="#f78f20"/></svg>
      <svg viewBox="0 0 12 12" aria-label="Mobile"><rect x="3" y="0.5" width="6" height="11" rx="1" fill="none" stroke="#f78f20" stroke-width="1.3"/><circle cx="6" cy="9.5" r="0.8" fill="#f78f20"/></svg>
      <svg viewBox="0 0 12 12" aria-label="Email"><rect x="0.8" y="2.5" width="10.4" height="7" fill="none" stroke="#f78f20" stroke-width="1.2"/><path d="M1 3l5 3.5L11 3" fill="none" stroke="#f78f20" stroke-width="1.2"/></svg>
      <svg viewBox="0 0 12 12" aria-label="Website"><circle cx="6" cy="6" r="5" fill="none" stroke="#f78f20" stroke-width="1.2"/><path d="M1 6h10M6 1c-2.5 3-2.5 7 0 10M6 1c2.5 3 2.5 7 0 10" fill="none" stroke="#f78f20" stroke-width="1"/></svg>
    </div>
  </section>
</main>
</body>
</html>
```